Enterprise Application UI beautification

We have an enterprise application that is being redesigned. A screenshot from the new UX/UI is provided. The current UI design is OK but we would like it to look better. The key goals of the UI are to look like a premium product (think luxury brand) and for it to be visually very appealing/attractive. When people see the UI we want them to have a significant, positive reaction. They should "ooh" and "ahh". This is a product sold to large enterprises, not consumers. The current UI is a little plain. The colors we want to use are blue, yellow, black, white and gray. We probably don't want different colors but feel free to use any variations within or close to that color scheme that you see fit. Also feel free to modify the spacing, icons, widgets, tables, fonts, etc.

Target Market(s)

Large enterprise customers (Summit 300).

Number of Pages Required

1 page

Font styles to use
Sans Serif

Colors
3277b5

Requirements
Must have
• A premium feel.

```html
<!DOCTYPE html>
<html lang="en">
<head>
<meta charset="utf-8">
<title>Skyforce - Sandbox</title>
<link rel="stylesheet" href="https://fonts.googleapis.com/css2?family=Source+Sans+3:wght@400;600;700&family=Source+Serif+4:wght@400;500&display=swap">
<style>
:root{
  --sand:#e9e4cc;
  --sand-deep:#d9d3a9;
  --sand-line:#d6cfae;
  --page:#f5f6f8;
  --panel:#eceef1;
  --row:#edf0f3;
  --ink:#3b4650;
  --ink-soft:#5b6670;
  --muted:#9aa4ad;
  --blue:#3277b5;
  --navy:#2e5873;
  --border:#dde1e6;
  --serif:"Source Serif 4",Georgia,serif;
  --sans:"Source Sans 3","Helvetica Neue",Arial,sans-serif;
}
*{box-sizing:border-box;margin:0;padding:0}
html,body{width:1200px;height:675px;overflow:hidden}
body{background:var(--page);font-family:var(--sans);color:var(--ink);position:relative}
.abs{position:absolute}
.sidebar{position:absolute;left:0;top:0;width:390px;height:675px;background:var(--sand)}
.brand{left:27px;top:14px;font-family:var(--sans);font-weight:700;font-size:17px;color:var(--navy);display:flex;align-items:center;gap:6px}
.brand .dot{width:12px;height:12px;border-radius:50%;background:var(--navy)}
.nav-item{left:26px;display:flex;align-items:center;gap:14px;font-size:10px;color:var(--muted);font-weight:600}
.nav-item svg{width:14px;height:14px;stroke:var(--muted);fill:none;stroke-width:1.4}
.nav-item.active{color:var(--navy);font-weight:700}
.nav-item.active svg{stroke:var(--navy)}
.src-title{left:174px;top:59px;font-family:var(--serif);font-size:17px;color:var(--ink)}
.add-link{display:flex;align-items:center;gap:5px;font-size:10px;font-weight:600;color:var(--blue)}
.add-link svg{width:12px;height:12px;stroke:currentColor;fill:none;stroke-width:1.3}
.search{left:175px;top:95px;width:215px;height:30px;background:var(--sand-deep);display:flex;align-items:center;padding-left:12px;gap:8px;font-size:10px;color:var(--ink)}
.search svg{width:12px;height:12px;stroke:var(--ink-soft);fill:none;stroke-width:1.5}
.src-list{left:174px;top:140px;width:176px}
.src{height:59px;border-bottom:1px solid var(--sand-line);padding-top:6px}
.src h3{font-family:var(--serif);font-weight:400;font-size:12.5px;color:var(--ink);line-height:16px;white-space:nowrap}
.src p{font-size:9.5px;color:var(--muted);margin-top:3px}
.scrollbar{left:376px;top:148px;width:3px;height:62px;background:var(--sand-line);border-radius:2px}
.crumbs{left:429px;top:20px;font-size:10px;color:var(--navy);display:flex;gap:10px;align-items:center}
.user{left:1090px;top:13px;display:flex;align-items:center;gap:8px;font-size:10px;color:var(--ink-soft)}
.avatar{width:25px;height:25px;border-radius:50%;background:linear-gradient(135deg,#7a8791,#c9b8a4)}
.page-title{left:429px;top:53px;font-family:var(--serif);font-size:22px;font-weight:400;color:var(--ink)}
.tools{left:658px;top:60px;display:flex;align-items:center;font-size:10px;font-weight:600;color:var(--muted)}
.tool{display:flex;align-items:center;gap:6px;padding:0 10px;border-left:1px solid var(--border)}
.tool:first-child{border-left:0;padding-left:0}
.tool svg{width:12px;height:12px;stroke:var(--muted);fill:none;stroke-width:1.3}
.btn{left:1064px;top:55px;width:110px;height:25px;background:var(--navy);color:#fff;font-size:10px;font-weight:700;display:flex;align-items:center;justify-content:center;gap:6px;border-radius:2px}
.btn svg{width:11px;height:11px;stroke:#fff;fill:none;stroke-width:1.4}
.info{left:430px;top:95px;width:745px;height:100px;background:var(--panel);border-radius:2px;font-size:9.5px}
.info dl{position:absolute;top:17px;display:grid;grid-template-columns:auto auto;row-gap:13.5px}
.info dt{font-weight:700;color:var(--ink-soft)}
.info dd{color:var(--ink-soft)}
.objs-title{left:429px;top:219px;font-family:var(--serif);font-size:17px;font-weight:400;color:var(--ink)}
.card{left:430px;width:744px;background:var(--page);border:1px solid var(--border);border-radius:2px}
.card-head{position:absolute;left:20px;display:flex;align-items:center;gap:9px;font-family:var(--serif);font-size:11px;font-weight:500;color:var(--ink)}
.mini{width:14px;height:14px;background:var(--row);display:flex;align-items:center;justify-content:center;border-radius:2px}
.mini svg{width:8px;height:8px;stroke:var(--blue);fill:none;stroke-width:1.4}
.chev{position:absolute;right:20px;width:11px;height:11px;stroke:var(--navy);fill:none;stroke-width:1.6}
.thead{position:absolute;top:44px;left:0;width:100%;font-size:8px;font-weight:700;letter-spacing:.6px;color:var(--muted)}
.thead span{position:absolute}
.trow{position:absolute;left:19px;width:704px;height:26px;background:var(--row);font-size:9.5px;color:var(--ink)}
.trow > *{position:absolute;top:50%;transform:translateY(-50%)}
.pk{width:14px;height:14px;background:#e2e6ea;border-radius:2px}
.pk svg{width:10px;height:10px;margin:2px;stroke:var(--ink-soft);fill:none;stroke-width:1.5}
.ic{display:flex;gap:7px;align-items:center}
.ic svg{width:9px;height:9px;stroke:var(--blue);fill:none;stroke-width:1.3}
.actions{left:648px;gap:10px}
</style>
</head>
<body>
<aside class="sidebar">
  <div class="abs brand"><span class="dot"></span>Vantix</div>

  <div class="abs nav-item" style="top:103px"><svg viewBox="0 0 14 14"><circle cx="7" cy="5" r="3"/><path d="M1.5 13c0-3 2.5-4.5 5.5-4.5s5.5 1.5 5.5 4.5z"/></svg>Menu option 1</div>
  <div class="abs nav-item" style="top:135px"><svg viewBox="0 0 14 14"><path d="M3.5 10H3a2.5 2.5 0 0 1 0-5 4 4 0 0 1 7.6-1A3 3 0 0 1 11 10h-.5M7 7v6M5 11l2 2 2-2"/></svg>Menu option 2</div>
  <div class="abs nav-item active" style="top:167px"><svg viewBox="0 0 14 14"><rect x="2" y="6" width="10" height="7" rx="1"/><path d="M3 4h8M4 2h6"/></svg>Menu option 3</div>
  <div class="abs nav-item" style="top:199px"><svg viewBox="0 0 14 14"><rect x="2" y="1.5" width="10" height="11" rx="1"/><path d="M4 5h2M8 5h2M4 9h2M8 9h2"/></svg>Menu option 4</div>
  <div class="abs nav-item" style="top:231px"><svg viewBox="0 0 14 14"><rect x="1.5" y="2.5" width="11" height="10" rx="1"/><path d="M1.5 6h11M5 6v6.5M9 6v6.5M1.5 9.2h11M4 1v3M10 1v3"/></svg>Menu option 5</div>
  <div class="abs nav-item" style="top:262px"><svg viewBox="0 0 14 14"><path d="M2 7a5 5 0 0 1 8.5-3.5L12 5M12 7a5 5 0 0 1-8.5 3.5L2 9M12 2v3H9M2 12V9h3"/></svg>Menu option 6</div>

  <div class="abs src-title">Data Sources</div>
  <div class="abs add-link" style="left:285px;top:64px"><svg viewBox="0 0 12 12"><circle cx="6" cy="6" r="5.3"/><path d="M6 3.3v5.4M3.3 6h5.4"/></svg>Add</div>

  <div class="abs search"><svg viewBox="0 0 12 12"><circle cx="7" cy="5" r="3.8"/><path d="M4.3 7.7 1 11"/></svg>Search...</div>

  <div class="abs src-list">
    <div class="src"><h3>Skyforce Sandbox</h3><p>Skyforce.io</p></div>
    <div class="src"><h3>Relbase Test 1 (administrator)</h3><p>Relbase DB</p></div>
    <div class="src"><h3>Relbase Test 2 (administrator)</h3><p>Relbase DB</p></div>
    <div class="src"><h3>Sadga</h3><p>Skyforce.io</p></div>
    <div class="src"><h3>Skyforce Test 1 (nasterd ev)</h3><p>Skyforce.io</p></div>
    <div class="src"><h3>SKFC – Field Entry Test</h3><p>Skyforce.io</p></div>
    <div class="src"><h3>SKFC 44</h3><p>Skyforce.io</p></div>
    <div class="src" style="border-bottom:0"><h3>SKFC 66</h3><p>Skyforce.io</p></div>
  </div>
  <div class="abs scrollbar"></div>
</aside>

<nav class="abs crumbs"><span>Menu Option 3</span><span style="color:var(--ink-soft)">›</span><span>Skyforce - Sandbox</span></nav>
<div class="abs user"><div class="avatar" role="img" aria-label="User profile photo"></div>Ned Norcross <span style="font-size:8px">⌄</span></div>

<h1 class="abs page-title">Skyforce – Sandbox</h1>
<div class="abs tools">
  <div class="tool"><svg viewBox="0 0 12 12"><path d="M2 10l1-3 6-6 2 2-6 6zM8 2l2 2"/></svg>Edit</div>
  <div class="tool"><svg viewBox="0 0 12 12"><rect x="1" y="4" width="7" height="7"/><path d="M4 4V1h7v7H8"/></svg>Clone</div>
  <div class="tool"><svg viewBox="0 0 12 12"><path d="M2 3h8M4.5 3V1.5h3V3M3 3l.5 8h5L9 3M5 5v4M7 5v4"/></svg>Delete</div>
</div>
<div class="abs btn"><svg viewBox="0 0 12 12"><path d="M7 1 2 7h4l-1 4 5-6H6z"/></svg>Test Connection</div>

<section class="abs info">
  <dl style="left:19px;column-gap:11px"><dt>Data source name:</dt><dd>Skyforce - Sandbox</dd><dt>Data source type:</dt><dd>Application</dd><dt>Status:</dt><dd>Active</dd></dl>
  <dl style="left:265px;column-gap:14px"><dt>Created by:</dt><dd>harlow.test</dd><dt>Last updated by:</dt><dd>harlow.test</dd><dt>Username:</dt><dd>leaddev@dev.northdata.net</dd></dl>
  <dl style="left:539px;column-gap:14px"><dt>Security token:</dt><dd>tadkaji4234ifndkn3</dd><dt>Environment type:</dt><dd>Production</dd><dt>Connected app:</dt><dd>No</dd></dl>
</section>

<h2 class="abs objs-title">Data Objects</h2>
<div class="abs add-link" style="left:536px;top:224px;color:var(--muted)"><svg viewBox="0 0 12 12"><circle cx="6" cy="6" r="5.3"/><path d="M6 3.3v5.4M3.3 6h5.4"/></svg>Add</div>

<section class="abs card" style="top:255px;height:199px">
  <div class="card-head" style="top:19px">Account
    <span class="mini"><svg viewBox="0 0 8 8"><circle cx="4" cy="4" r="3.5"/><path d="M4 2v4M2 4h4"/></svg></span>
    <span class="mini"><svg viewBox="0 0 8 8"><path d="M1 2h6M2 2l.5 5.5h3L6 2M3 1h2"/></svg></span>
  </div>
  <svg class="chev" style="top:21px" viewBox="0 0 11 11"><path d="M1 8l4.5-4.5L10 8"/></svg>
  <div class="thead"><span style="left:19px">FIELD NAME</span><span style="left:224px">DATA TYPE</span><span style="left:397px">PRIMARY KEY</span><span style="left:487px">RULE TYPES</span><span style="left:572px">SENSITIVE DATA</span><span style="left:674px">ACTIONS</span></div>

  <div class="trow" style="top:59px"><span style="left:10px">Account description</span><span style="left:205px">Common, Text</span><div class="pk" style="left:378px"><svg viewBox="0 0 10 10"><path d="M1.5 5l2.5 2.5L8.5 2.5"/></svg></div><div class="ic" style="left:467px"><svg viewBox="0 0 9 9"><path d="M1 8 4 1l3 7M2.3 5.5h3.4"/></svg><svg viewBox="0 0 9 9"><rect x="1" y="4" width="4" height="4"/><path d="M4 1h4v4"/></svg><svg viewBox="0 0 9 9" style="stroke:var(--ink-soft)"><path d="M2 3l2.5 2.5L7 3"/></svg></div><div class="ic" style="left:562px"><svg viewBox="0 0 9 9" style="stroke:var(--ink-soft)"><path d="M2 3l2.5 2.5L7 3"/></svg></div><div class="ic actions"><svg viewBox="0 0 9 9"><path d="M1 8l1-2.5L6.5 1 8 2.5 3.5 7z"/></svg><svg viewBox="0 0 9 9"><path d="M1 2h7M2 2l.5 6.5h4L7 2M3.5 1h2"/></svg></div></div>

  <div class="trow" style="top:90px"><span style="left:10px">Account Fax</span><span style="left:205px">Address, Address Line 3</span><div class="pk" style="left:378px"></div><div class="ic" style="left:467px"><svg viewBox="0 0 9 9"><rect x="1" y="4" width="4" height="4"/><path d="M4 1h4v4"/></svg></div><div class="ic actions"><svg viewBox="0 0 9 9"><path d="M1 8l1-2.5L6.5 1 8 2.5 3.5 7z"/></svg><svg viewBox="0 0 9 9"><path d="M1 2h7M2 2l.5 6.5h4L7 2M3.5 1h2"/></svg></div></div>

  <div class="trow" style="top:121px"><span style="left:10px">Account ID</span><span style="left:205px">Common ID</span><div class="pk" style="left:378px"></div><div class="ic" style="left:467px"><svg viewBox="0 0 9 9"><path d="M1 8 4 1l3 7M2.3 5.5h3.4"/></svg><svg viewBox="0 0 9 9"><rect x="1" y="4" width="4" height="4"/><path d="M4 1h4v4"/></svg></div><div class="ic actions"><svg viewBox="0 0 9 9"><path d="M1 8l1-2.5L6.5 1 8 2.5 3.5 7z"/></svg><svg viewBox="0 0 9 9"><path d="M1 2h7M2 2l.5 6.5h4L7 2M3.5 1h2"/></svg></div></div>

  <div class="trow" style="top:152px"><span style="left:10px">Account Name</span><span style="left:205px">Address, Address Line 2</span><div class="pk" style="left:378px"></div><div class="ic" style="left:467px"><svg viewBox="0 0 9 9"><rect x="1" y="4" width="4" height="4"/><path d="M4 1h4v4"/></svg></div><div class="ic actions"><svg viewBox="0 0 9 9"><path d="M1 8l1-2.5L6.5 1 8 2.5 3.5 7z"/></svg><svg viewBox="0 0 9 9"><path d="M1 2h7M2 2l.5 6.5h4L7 2M3.5 1h2"/></svg></div></div>
</section>

<section class="abs card" style="top:465px;height:30px"><div class="card-head" style="top:7px">Asset <span class="mini"><svg viewBox="0 0 8 8"><path d="M1 2h6M2 2l.5 5.5h3L6 2M3 1h2"/></svg></span></div><svg class="chev" style="top:9px" viewBox="0 0 11 11"><path d="M1 3.5l4.5 4.5L10 3.5"/></svg></section>
<section class="abs card" style="top:505px;height:30px"><div class="card-head" style="top:7px">Asset Relationship <span class="mini"><svg viewBox="0 0 8 8"><path d="M1 2h6M2 2l.5 5.5h3L6 2M3 1h2"/></svg></span></div><svg class="chev" style="top:9px" viewBox="0 0 11 11"><path d="M1 3.5l4.5 4.5L10 3.5"/></svg></section>
<section class="abs card" style="top:545px;height:30px"><div class="card-head" style="top:7px">Asset Token Event <span class="mini"><svg viewBox="0 0 8 8"><path d="M1 2h6M2 2l.5 5.5h3L6 2M3 1h2"/></svg></span></div><svg class="chev" style="top:9px" viewBox="0 0 11 11"><path d="M1 3.5l4.5 4.5L10 3.5"/></svg></section>
<section class="abs card" style="top:585px;height:30px"><div class="card-head" style="top:7px">Case <span class="mini"><svg viewBox="0 0 8 8"><path d="M1 2h6M2 2l.5 5.5h3L6 2M3 1h2"/></svg></span></div><svg class="chev" style="top:9px" viewBox="0 0 11 11"><path d="M1 3.5l4.5 4.5L10 3.5"/></svg></section>
</body>
</html>
```